October Billboard TX

Billboard - creative design using company colors. Previous billboard graphic is included for reference along with a rough example of the requested "less busy" design. Required graphics for the simple billboard design are also included in the upload. Billboard dimensions are attached. Need this design ASAP!

```html
<!DOCTYPE html>
<html lang="en">
<head>
<meta charset="utf-8">
<title>Bright Sight Kids' Eye Clinic – Billboard</title>
<link rel="stylesheet" href="https://fonts.googleapis.com/css2?family=Montserrat:ital,wght@0,400;0,700;0,800;1,300;1,900&display=swap">
<style>
  :root {
    --brand-blue: #0a6ab6;
    --brand-red: #e8443f;
    --ink: #111111;
    --paper: #ffffff;
    --photo-warm: #8a7468;
    --photo-light: #d9d2cb;
    --photo-dark: #3a2b25;
  }
  * { margin: 0; padding: 0; box-sizing: border-box; }
  html, body { width: 1200px; height: 600px; overflow: hidden; background: var(--paper); }
  .billboard {
    position: relative; width: 1200px; height: 600px; overflow: hidden;
    background: var(--paper); font-family: 'Montserrat', sans-serif; color: var(--ink);
  }
  .swoosh-layer { position: absolute; inset: 0; width: 1200px; height: 600px; }

  .brand {
    position: absolute; left: 34px; top: 38px;
    display: flex; align-items: center; gap: 16px;
    color: var(--brand-blue); font-weight: 800; text-transform: uppercase;
  }
  .brand-dot { width: 44px; height: 44px; border-radius: 50%; background: var(--brand-blue); flex: none; }
  .brand-name { font-size: 36px; line-height: 1.08; letter-spacing: 0.5px; }

  .kids-badge {
    position: absolute; left: 518px; top: 34px; width: 164px; height: 164px;
    border-radius: 50%; border: 9px solid var(--brand-red);
    display: flex; align-items: center; justify-content: center; text-align: center;
    font-weight: 800; font-size: 34px; line-height: 1.05; color: var(--ink);
  }

  .quote-band {
    position: absolute; left: 0; top: 215px; width: 745px; height: 106px;
    background: var(--brand-red); border-radius: 0 53px 53px 0;
    box-shadow: 4px 0 0 var(--paper), 8px 0 0 var(--brand-red);
    padding: 10px 0 0 30px; color: var(--paper);
  }
  .quote-text { font-style: italic; font-weight: 900; font-size: 27.5px; line-height: 29.5px; text-transform: uppercase; letter-spacing: -0.2px; }
  .quote-text .light { font-weight: 300; }
  .quote-author { font-style: normal; font-weight: 400; font-size: 19px; margin-left: 8px; }

  .age-list {
    position: absolute; left: 30px; top: 334px;
    display: grid; grid-template-columns: 248px auto; row-gap: 4px;
    list-style: none; font-weight: 700; font-size: 32px; line-height: 36px; text-transform: uppercase;
  }
  .age-list li::before { content: "• "; }

  .appointments { position: absolute; left: 44px; top: 494px; color: var(--paper); }
  .appointments-label { margin-left: 38px; font-weight: 700; font-size: 26px; letter-spacing: 1px; text-transform: uppercase; }
  .appointments-phone { display: flex; align-items: center; gap: 6px; font-weight: 800; font-size: 57px; line-height: 60px; }
  .phone-icon { width: 34px; height: 34px; }

  .photo {
    position: absolute; left: 728px; top: 68px; width: 472px; height: 532px;
    border-radius: 220px 220px 0 40px;
    background: radial-gradient(ellipse at 55% 40%, var(--photo-light) 0%, var(--photo-warm) 55%, var(--photo-dark) 100%);
  }

  .spanish-badge {
    position: absolute; left: 843px; top: 20px; width: 357px; height: 88px;
    background: var(--brand-blue); border-radius: 20px 0 0 20px;
    padding: 14px 30px 0 0; text-align: right; color: var(--paper);
    font-weight: 700; font-size: 27px; line-height: 30px; text-transform: uppercase; letter-spacing: 0.5px;
  }
</style>
</head>
<body>
<main class="billboard">
  <svg class="swoosh-layer" viewBox="0 0 1200 600" aria-hidden="true">
    <path d="M0,452 C180,418 360,420 462,468 C330,442 160,456 0,505 Z" fill="var(--brand-blue)"/>
    <path d="M0,520 C220,440 520,440 740,532 L740,600 L0,600 Z" fill="var(--brand-red)"/>
    <path d="M1200,425 L1178,448 L1200,505 Z" fill="var(--brand-blue)"/>
  </svg>

  <header class="brand">
    <span class="brand-dot"></span>
    <span class="brand-name">Bright Sight<br>Kids' Eye Clinic<br>of El Paso</span>
  </header>

  <div class="kids-badge">KIDS<br>ONLY</div>

  <section class="quote-band">
    <p class="quote-text">"I take my child to El Paso's most qualified <span class="light">and</span> experienced pediatric eye doctor." <span class="quote-author">M. REYES</span></p>
  </section>

  <ul class="age-list">
    <li>Newborns</li>
    <li>Toddlers</li>
    <li>Infants</li>
    <li>Tweens &amp; Teens</li>
  </ul>

  <section class="appointments">
    <p class="appointments-label">For appointments call</p>
    <p class="appointments-phone">
      <svg class="phone-icon" viewBox="0 0 24 24" aria-hidden="true">
        <path d="M6.6 10.8a15.1 15.1 0 0 0 6.6 6.6l2.2-2.2a1 1 0 0 1 1-.25 11.4 11.4 0 0 0 3.6.57 1 1 0 0 1 1 1V20a1 1 0 0 1-1 1A17 17 0 0 1 3 4a1 1 0 0 1 1-1h3.5a1 1 0 0 1 1 1c0 1.25.2 2.45.57 3.57a1 1 0 0 1-.25 1z" fill="var(--paper)"/>
      </svg>
      (915) 555-0142
    </p>
  </section>

  <div class="photo" role="img" aria-label="Photo of a smiling mother in glasses holding a baby wearing round glasses"></div>

  <div class="spanish-badge">La doctora habla<br>español</div>
</main>
</body>
</html>
```